OSB - Brochure 52 week Curriculum

Oakstone Brotherhood, Inc. wants to create a distribution Brochure. In the Bible (Matthew 28:18-20)- JESUS said to "TEACH" others what HE has commanded. we want to "PUT IN PRINT"

these 52 lines summarize HIS teachings
we want to use as our Curriculum teaching men ...

incorporate our statements and two main passages of scripture
(see attach pictures of headquarter lobby) to brand uniformity and consistency... we have summarized into 52 groups, but its NOT required to have numbers...
Purpose = obey GOD
Mission = love others
Vision = Development God fearing men globally.

The designer can have freedom in layout and sizing.
we were thinking bi fold , but again... designer has freedom
Please incorporate our colors (white, black, gray) using color wheel provided and our LOGO with website.

```html
<!DOCTYPE html>
<html lang="en">
<head>
<meta charset="UTF-8">
<title>Oakstone Brotherhood – Curriculum Brochure Spread</title>
<link href="https://fonts.googleapis.com/css2?family=Poppins:ital,wght@0,400;0,600;0,700;1,400;1,800&display=swap" rel="stylesheet">
<style>
  :root {
    --backdrop: #b3d3d4;
    --ink-black: #141414;
    --ink-dark: #1f1f1f;
    --gray-panel: #b9b9b9;
    --gray-text: #2a2a2a;
    --heading-dark: #222a2e;
    --white: #ffffff;
    --soft-white: #e6e6e6;
  }
  * { box-sizing: border-box; margin: 0; padding: 0; }
  html, body { width: 1200px; height: 700px; overflow: hidden; }
  body {
    background: var(--backdrop);
    font-family: "Poppins", sans-serif;
    position: relative;
  }
  .spread {
    position: absolute;
    left: 20px; top: 156px;
    width: 1160px; height: 388px;
    display: flex;
    box-shadow: 0 10px 24px rgba(0,0,0,0.18);
  }
  .page {
    position: relative;
    width: 580px; height: 388px;
    overflow: hidden;
    background: var(--ink-black);
  }
  .page--left { border-right: 1px solid #2c2c2c; }

  /* image placeholders */
  .photo {
    position: absolute;
  }
  .photo--prayer {
    left: 0; top: 0; width: 290px; height: 388px;
    background: radial-gradient(ellipse at 45% 40%, #8a8a8a 0%, #4a4a4a 35%, #1a1a1a 75%, #141414 100%);
  }
  .photo--brothers {
    left: 240px; top: 0; width: 340px; height: 388px;
    background: linear-gradient(90deg, #2a2a2a 0%, #6f6f6f 30%, #9a9a9a 60%, #7a7a7a 100%);
  }
  .page--right .fade {
    position: absolute; left: 0; bottom: 0; width: 580px; height: 160px;
    background: linear-gradient(0deg, #161616 0%, rgba(22,22,22,0.6) 60%, rgba(22,22,22,0) 100%);
  }

  /* content */
  .section-title {
    font-weight: 800;
    font-style: italic;
    text-transform: uppercase;
    line-height: 1.05;
    letter-spacing: 0.2px;
  }
  .page--left .section-title {
    position: absolute; left: 308px; top: 22px;
    font-size: 16px; color: var(--soft-white);
  }
  .points {
    list-style: none;
    position: absolute;
  }
  .points li {
    position: relative;
    padding-left: 18px;
    font-size: 8px;
    font-style: italic;
    line-height: 1.28;
    margin-bottom: 8px;
  }
  .points .chevron {
    position: absolute; left: 0; top: 1px;
    width: 10px; height: 9px;
  }
  .page--left .points {
    left: 300px; top: 60px; width: 258px;
    color: var(--soft-white);
  }
  .page--left .chevron path { fill: var(--white); }

  .info-panel {
    position: absolute; left: 0; top: 0;
    width: 250px; height: 225px;
    background: var(--gray-panel);
  }
  .page--right .section-title {
    position: absolute; left: 22px; top: 22px; width: 220px;
    font-size: 14px; color: var(--heading-dark);
  }
  .page--right .points {
    left: 22px; top: 70px; width: 218px;
    color: var(--gray-text);
  }
  .page--right .chevron path { fill: var(--ink-black); }

  /* footer */
  .brand-name {
    position: absolute; bottom: 24px;
    font-size: 14px; font-weight: 700;
    color: var(--white);
    letter-spacing: 0.5px;
  }
  .page--left .brand-name { left: 28px; }
  .page--right .brand-name { left: 24px; }
  .page-meta {
    position: absolute; bottom: 28px; right: 26px;
    font-size: 8px; color: var(--soft-white);
  }
  .page-meta strong { font-weight: 600; }
  .page-meta .divider { margin: 0 8px; }
</style>
</head>
<body>
  <main class="spread">
    <section class="page page--left">
      <div class="photo photo--prayer" role="img" aria-label="Black and white photo of a man praying with clasped hands holding a cross pendant"></div>
      <h2 class="section-title">Prayer</h2>
      <ul class="points">
        <li><svg class="chevron" viewBox="0 0 10 9"><path d="M0 0h3l4 4.5L3 9H0l4-4.5z M4 0h2l4 4.5L6 9H4l4-4.5z"/></svg>Jesus provided guidance on prayer, teaching that it should be done in private and with sincerity (Matthew 6:5-8).</li>
        <li><svg class="chevron" viewBox="0 0 10 9"><path d="M0 0h3l4 4.5L3 9H0l4-4.5z M4 0h2l4 4.5L6 9H4l4-4.5z"/></svg>He also linked prayer to having a forgiving heart (Mark 11:25; Matthew 18:18-20). HE encouraged praying with simple faith and persistence (Luke 11:5-13; Matthew 21:21-22).</li>
        <li><svg class="chevron" viewBox="0 0 10 9"><path d="M0 0h3l4 4.5L3 9H0l4-4.5z M4 0h2l4 4.5L6 9H4l4-4.5z"/></svg>Pray: Engage in prayer consistently, with sincerity and according to Jesus' example.</li>
        <li><svg class="chevron" viewBox="0 0 10 9"><path d="M0 0h3l4 4.5L3 9H0l4-4.5z M4 0h2l4 4.5L6 9H4l4-4.5z"/></svg>Prayer for our enemies : Luke 23:24, Matthew 5:44</li>
        <li><svg class="chevron" viewBox="0 0 10 9"><path d="M0 0h3l4 4.5L3 9H0l4-4.5z M4 0h2l4 4.5L6 9H4l4-4.5z"/></svg>Pray for others : intercession</li>
        <li><svg class="chevron" viewBox="0 0 10 9"><path d="M0 0h3l4 4.5L3 9H0l4-4.5z M4 0h2l4 4.5L6 9H4l4-4.5z"/></svg>Pray for laborers: Seek God to send workers into the harvest field of souls. Pray for kingdom laborers: Matthew 9:38, Luke 10:2</li>
      </ul>
      <div class="brand-name">OSB</div>
      <div class="page-meta"><strong>Page 8</strong><span class="divider">|</span>oakstonebrotherhood.org</div>
    </section>

    <section class="page page--right">
      <div class="photo photo--brothers" role="img" aria-label="Black and white photo of three smiling men running together"></div>
      <div class="fade"></div>
      <div class="info-panel"></div>
      <h2 class="section-title">Regarding Outreach and Discipleship</h2>
      <ul class="points">
        <li><svg class="chevron" viewBox="0 0 10 9"><path d="M0 0h3l4 4.5L3 9H0l4-4.5z M4 0h2l4 4.5L6 9H4l4-4.5z"/></svg>Go and make disciples of all nations: Evangelize and teach others to follow Jesus' commands: This is a central command, emphasizing the importance of evangelism and discipleship. Matthew 28:18-20. Teach others to obey all that Jesus commanded: Passing on the teachings of Christ to new believers is a key aspect of discipleship.</li>
        <li><svg class="chevron" viewBox="0 0 10 9"><path d="M0 0h3l4 4.5L3 9H0l4-4.5z M4 0h2l4 4.5L6 9H4l4-4.5z"/></svg>Feed My Sheep: Care for and nourish the spiritual lives of believers.</li>
        <li><svg class="chevron" viewBox="0 0 10 9"><path d="M0 0h3l4 4.5L3 9H0l4-4.5z M4 0h2l4 4.5L6 9H4l4-4.5z"/></svg>Receive God's power: Be filled with the Holy Spirit to effectively carry out God's work.</li>
      </ul>
      <div class="brand-name">OSB</div>
      <div class="page-meta"><strong>Page 9</strong><span class="divider">|</span>oakstonebrotherhood.org</div>
    </section>
  </main>
</body>
</html>
```